Business Card Design Project

A business card for a new company in Ontario Canada called Build for Growth. It is a consulting company which uses Brixo as the medium for facilitation.

The target market is for senior leaders in healthcare and social services.

Industry/Entity Type

Healthcare

Requirements
Must have
• The name Build For Growth
Dana Montreuil RRT, B Ed (AD ed).
Tacticraft Facililitator (R)

Tag Line
Engaging Transforming and Innovative
The attached logo

danamontreuil@examplemail.com
416-555-0147
Should not have
• Lime green
Times New Roman or Arial font
Do not include Brixo bricks on the card.

```html
<!DOCTYPE html>
<html lang="en">
<head>
<meta charset="utf-8">
<title>Build For Growth – Business Card Concepts</title>
<link rel="stylesheet" href="https://fonts.googleapis.com/css2?family=Didact+Gothic&family=Open+Sans:wght@400;700&display=swap">
<style>
  :root {
    --purple: #5e2b86;
    --white: #ffffff;
    --ink: #1f1f1f;
    --border: #7a7a7a;
    --band-grey: #d6d6d6;
    --mark-blue: #3ea3d9;
  }
  html, body {
    margin: 0;
    padding: 0;
    width: 1200px;
    height: 2731px;
    overflow: hidden;
    background: var(--white);
  }
  .sheet {
    position: relative;
    width: 1200px;
    height: 2731px;
  }
  .card {
    position: absolute;
    left: 63px;
    width: 1104px;
    height: 597px;
    box-sizing: border-box;
    border: 3px solid var(--border);
    background: var(--white);
    overflow: hidden;
    color: var(--ink);
  }
  .card--one   { top: 57px; }
  .card--two   { top: 726px; }
  .card--three { top: 1404px; }
  .card--four  { top: 2064px; }

  .card__header {
    position: absolute;
    left: 0; top: 0;
    width: 100%;
    height: 240px;
    background: var(--purple);
    color: var(--white);
  }
  .rounded { font-family: "Didact Gothic", sans-serif; }
  .sans    { font-family: "Open Sans", sans-serif; }

  .line { position: absolute; margin: 0; white-space: nowrap; line-height: 1; }
  .centered { width: 600px; text-align: center; }

  /* Classic header layout (cards one and two) */
  .classic .name     { left: 36px; top: 34px; font-size: 53px; }
  .classic .role     { left: 147px; top: 90px; font-size: 32px; }
  .classic .email    { left: 130px; top: 144px; font-size: 35px; }
  .classic .phone    { left: 130px; top: 184px; font-size: 35px; }
  .classic .tagline  { left: 36px; top: 520px; font-size: 40px; }

  /* Band layout (card three) */
  .band { position: absolute; left: 0; top: 0; }
  .banded .name    { left: 372px; top: 68px; font-size: 38px; font-weight: 700; color: var(--purple); }
  .banded .role    { left: 402px; top: 118px; font-size: 30px; }
  .banded .email   { left: 402px; top: 180px; font-size: 32px; }
  .banded .phone   { left: 402px; top: 225px; font-size: 32px; }
  .banded .tagline { left: 477px; top: 524px; font-size: 30px; }

  /* Bold header layout (card four) */
  .bold .name    { left: 36px; top: 22px; font-size: 40px; font-weight: 700; }
  .bold .role    { left: 72px; top: 77px; font-size: 30px; }
  .bold .email   { left: 72px; top: 134px; font-size: 33px; }
  .bold .phone   { left: 72px; top: 179px; font-size: 33px; }
  .bold .tagline { left: 36px; top: 527px; font-size: 34px; }

  /* Brand name block in place of the mark */
  .brand {
    position: absolute;
    left: 729px;
    top: 272px;
    width: 300px;
    display: flex;
    flex-direction: column;
    align-items: center;
    gap: 24px;
  }
  .banded .brand { left: 39px; top: 70px; }
  .brand__dot {
    width: 180px;
    height: 180px;
    border-radius: 50%;
    background: var(--mark-blue);
  }
  .brand__name {
    margin: 0;
    font-size: 34px;
    line-height: 1.15;
    text-align: center;
    color: var(--purple);
  }
</style>
</head>
<body>
<main class="sheet">

  <section class="card card--one classic rounded">
    <header class="card__header">
      <p class="line name">Dana Montreuil RRT, B Ed (AD ed).</p>
      <p class="line centered role">Tacticraft Facilitator (R)</p>
      <p class="line centered email">danamontreuil@examplemail.com</p>
      <p class="line centered phone">416-555-0147</p>
    </header>
    <div class="brand">
      <span class="brand__dot"></span>
      <p class="brand__name">Build For Growth</p>
    </div>
    <p class="line tagline">Engaging Transforming and Innovative</p>
  </section>

  <section class="card card--two classic rounded">
    <header class="card__header">
      <p class="line name">Dana Montreuil RRT, B Ed (AD ed).</p>
      <p class="line centered role">Tacticraft Facilitator (R)</p>
      <p class="line centered email">danamontreuil@examplemail.com</p>
      <p class="line centered phone">416-555-0147</p>
    </header>
    <div class="brand">
      <span class="brand__dot"></span>
      <p class="brand__name">Build For Growth</p>
    </div>
    <p class="line tagline">Engaging Transforming and Innovative</p>
  </section>

  <section class="card card--three banded sans">
    <svg class="band" width="1104" height="597" viewBox="0 0 1104 597" aria-hidden="true">
      <polygon points="8,0 258,0 408,597 63,597" fill="var(--band-grey)"/>
    </svg>
    <div class="brand">
      <span class="brand__dot"></span>
      <p class="brand__name">Build For Growth</p>
    </div>
    <p class="line name">Dana Montreuil RRT, B Ed (AD ed).</p>
    <p class="line centered role">Tacticraft Facilitator (R)</p>
    <p class="line centered email">danamontreuil@examplemail.com</p>
    <p class="line centered phone">416-555-0147</p>
    <p class="line tagline">Engaging Transforming and Innovative</p>
  </section>

  <section class="card card--four bold sans">
    <header class="card__header">
      <p class="line name">Dana Montreuil RRT, B Ed (AD ed).</p>
      <p class="line centered role">Tacticraft Facilitator (R)</p>
      <p class="line centered email">danamontreuil@examplemail.com</p>
      <p class="line centered phone">416-555-0147</p>
    </header>
    <div class="brand">
      <span class="brand__dot"></span>
      <p class="brand__name">Build For Growth</p>
    </div>
    <p class="line tagline">Engaging Transforming and Innovative</p>
  </section>

</main>
</body>
</html>
```